Homepage/Landing Page for Vellamark.com

We need a brochure style landing page for our website, vellamark.com. The new homepage will direct people either to quarrytonpress.com (a website for businesses to purchase printing), to a landing page about trading cards/sports memorabilia, or to a website about high-end embellished cartons/boxes.
The existing site, www.vellamark.com, will become quarrytonpress.com, and people arriving at vellamark.com will be shown three options to choose based on their needs:
1) Business Printing - for everyone from micro-businesses on up, our manufacturing process insures we have something to suit every business.
2) Highly decorated and embellished cartons - perfect for new brands, prototypes, pilot programs, seasonal packaging
3) Trading cards/sports memorabilia - Handling cards for athletes from Junior Circuit to high school, college and beyond.

Target Market(s)

Target market is small business owners and print buyers

Industry/Entity Type

Printing and Packaging

Number of Pages Required

1 page

Font styles to use
Other font styles liked:
• See the VM Web Flip Standards PDF attached.

Requirements
Must have
• 3 clearly marked paths for customers to follow - use web standards pdf below for fonts and colors
Should not have
• My project should not feel trendy or faddish, but modern and professional.

```html
<!DOCTYPE html>
<html lang="en">
<head>
<meta charset="utf-8">
<title>Vellamark — Positively Different.</title>
<link rel="stylesheet" href="https://fonts.googleapis.com/css2?family=Domine:wght@400;700&family=Questrial&display=swap">
<style>
  :root {
    --teal: #17a9c4;
    --teal-dark: #2f8f8c;
    --ink: #1a1a1a;
    --text: #333;
    --muted: #555;
    --pale-blue: #d6e8ee;
    --pale-aqua: #e2f2f3;
    --band: #64b2ca;
    --line: #dcdcdc;
    --white: #fff;
  }
  * { box-sizing: border-box; margin: 0; padding: 0; }
  html, body { width: 1200px; height: 2426px; overflow: hidden; background: var(--white); }
  body { font-family: "Questrial", sans-serif; color: var(--text); }
  .page { position: relative; width: 1200px; height: 2426px; overflow: hidden; }
  .abs { position: absolute; }
  .serif { font-family: "Domine", serif; }

  /* header */
  .brand { left: 88px; top: 40px; display: flex; align-items: center; gap: 8px;
    font-family: "Domine", serif; font-weight: 700; font-size: 24px; color: var(--teal); }
  .brand-square { width: 16px; height: 16px; background: var(--teal); }
  .nav { top: 34px; left: 690px; display: flex; gap: 36px; font-size: 15px; font-weight: 700; color: var(--ink); letter-spacing: .2px; }
  .call { left: 932px; top: 26px; display: flex; align-items: center; gap: 8px; }
  .call-text { font-size: 14px; font-weight: 700; color: var(--ink); line-height: 18px; }
  .search { left: 1093px; top: 33px; }

  /* hero */
  .hero-photo { left: 523px; top: 88px; width: 677px; height: 637px;
    background: linear-gradient(120deg, #eef1ee 0%, #d7d9d3 35%, #b989c9 55%, #8fa6c9 70%, #d99a3e 90%, #f0ede8 100%); }
  .dots-field { left: 476px; top: 531px; width: 47px; height: 246px; background: #bfe7ef; }
  .dots-field-base { left: 523px; top: 725px; width: 74px; height: 52px; background: #bfe7ef; }
  .hero-kicker { left: 88px; top: 370px; font-size: 26px; color: var(--teal); }
  .hero-title { left: 88px; top: 405px; font-size: 74px; font-weight: 700; line-height: 80px; color: var(--ink); letter-spacing: .5px; }

  /* path cards */
  .path-card { top: 860px; width: 330px; height: 303px; background: var(--white);
    box-shadow: 0 18px 30px -12px rgba(23,169,196,.22), 0 0 20px rgba(0,0,0,.04); text-align: center; }
  .path-card.business { left: 88px; }
  .path-card.cartons { left: 435px; }
  .path-card.cards { left: 782px; }
  .path-icon { position: absolute; left: 50%; top: 56px; transform: translateX(-50%); }
  .path-title { position: absolute; top: 156px; width: 100%; font-size: 24px; color: var(--ink); }
  .path-desc { position: absolute; top: 193px; left: 36px; right: 36px; font-size: 15px; line-height: 20px; color: var(--text); }

  /* feature pair */
  .proof-panel { left: 0; top: 1286px; width: 600px; height: 509px; background: var(--pale-blue); }
  .tint-panel { left: 600px; top: 1286px; width: 600px; height: 509px; background: var(--pale-aqua); }
  .proof-name { left: 0; width: 585px; top: 1392px; text-align: center; font-size: 40px; line-height: 40px; color: var(--teal-dark); }
  .proof-desc { left: 140px; width: 305px; top: 1488px; text-align: center; font-size: 15px; line-height: 20px; }
  .proof-photo { left: 0; top: 1560px; width: 600px; height: 235px;
    background: linear-gradient(160deg, rgba(214,232,238,0) 0%, #d9d9d9 40%, #8a8f8f 75%, #4d6a6e 100%); }
  .tint-name { left: 663px; top: 1516px; font-size: 46px; color: #6a6a6a; }
  .tint-desc { left: 663px; top: 1580px; width: 262px; font-size: 15px; line-height: 20px; }
  .tint-photo { left: 945px; top: 1305px; width: 255px; height: 490px;
    background: linear-gradient(200deg, #2a7f80 0%, #333 30%, #f2f2f2 50%, #f3c23a 65%, #f08a2a 85%, #e8e4dc 100%); }

  /* prototyping band */
  .proto-band { left: 0; top: 1795px; width: 1200px; height: 223px; background: var(--band); }
  .proto-photo { left: 700px; top: 1795px; width: 500px; height: 223px;
    background: linear-gradient(110deg, rgba(100,178,202,0) 0%, #d8dcdc 30%, #efefef 55%, #3a3d40 75%, #e9eaea 100%); }
  .proto-title { left: 88px; top: 1884px; font-size: 29px; color: var(--white); }
  .proto-sub { left: 88px; top: 1930px; font-size: 15px; color: var(--white); }

  /* footer */
  .foot-brand { left: 170px; top: 2196px; display: flex; align-items: center; gap: 8px;
    font-family: "Domine", serif; font-weight: 700; font-size: 22px; color: var(--teal); }
  .foot-col { top: 2130px; }
  .foot-col h3 { font-family: "Domine", serif; font-weight: 400; font-size: 19px; color: var(--ink); margin-bottom: 10px; }
  .foot-col li { list-style: none; font-size: 13px; line-height: 22px; color: var(--text); }
  .foot-col.expect { left: 361px; }
  .foot-col.about { left: 604px; }
  .foot-col.contact { left: 826px; }
  .contact li { display: flex; gap: 7px; align-items: flex-start; }
  .contact svg { margin-top: 5px; flex: none; }
  .contact .indent { padding-left: 19px; }
  .foot-rule { left: 88px; top: 2364px; width: 1024px; height: 1px; background: var(--line); }
  .copyright { left: 0; width: 1200px; top: 2385px; text-align: center; font-size: 16px; color: var(--ink); }
  .chat { left: 1126px; top: 2338px; width: 52px; height: 52px; border-radius: 50%; background: var(--teal);
    display: flex; align-items: center; justify-content: center; box-shadow: 0 3px 8px rgba(0,0,0,.15); }
</style>
</head>
<body>
<div class="page">

  <header>
    <div class="abs brand"><span class="brand-square"></span>vellamark</div>
    <nav class="abs nav"><span>About Us</span><span>How to Reach Us</span></nav>
    <div class="abs call">
      <svg width="26" height="26" viewBox="0 0 24 24" aria-hidden="true"><path fill="#17a9c4" d="M6.6 10.8a15.1 15.1 0 0 0 6.6 6.6l2.2-2.2c.3-.3.7-.4 1-.2 1.1.4 2.3.6 3.6.6.6 0 1 .4 1 1V20c0 .6-.4 1-1 1A17 17 0 0 1 3 4c0-.6.4-1 1-1h3.5c.6 0 1 .4 1 1 0 1.3.2 2.5.6 3.6.1.3 0 .7-.2 1z"/></svg>
      <div class="call-text">Call Us!<br>(855-555-0148)</div>
    </div>
    <svg class="abs search" width="18" height="18" viewBox="0 0 18 18" aria-hidden="true"><circle cx="7.5" cy="7.5" r="6" fill="none" stroke="#1a1a1a" stroke-width="2"/><line x1="12" y1="12" x2="16.5" y2="16.5" stroke="#1a1a1a" stroke-width="2.2" stroke-linecap="round"/></svg>
  </header>

  <section class="hero">
    <div class="abs dots-field" aria-hidden="true"></div>
    <div class="abs dots-field-base" aria-hidden="true"></div>
    <div class="abs hero-photo" role="img" aria-label="Photo of two designers reviewing a print job at a desk in a bright studio"></div>
    <p class="abs hero-kicker serif">vellamark</p>
    <h1 class="abs hero-title serif">Positively<br>&nbsp;Different.</h1>
  </section>

  <section class="paths">
    <a class="abs path-card business">
      <div class="path-icon" role="img" aria-label="Business printing icon" style="width:72px;height:80px;background:#3d9e99;"></div>
      <h2 class="path-title serif">Business Printing</h2>
      <p class="path-desc">For everyone from micro-businesses and beyond, we have something to suit everyone.</p>
    </a>
    <a class="abs path-card cartons">
      <svg class="path-icon" width="80" height="80" viewBox="0 0 80 80" role="img" aria-label="Carton box icon">
        <rect x="6" y="22" width="68" height="54" rx="3" fill="none" stroke="#17a9c4" stroke-width="3"/>
        <line x1="6" y1="38" x2="74" y2="38" stroke="#17a9c4" stroke-width="3"/>
        <line x1="40" y1="6" x2="40" y2="38" stroke="#17a9c4" stroke-width="3"/>
      </svg>
      <h2 class="path-title serif">Embellished Cartons</h2>
      <p class="path-desc">Highly decorated cartons for new brands, prototypes, pilot programs and seasonal packaging.</p>
    </a>
    <a class="abs path-card cards">
      <svg class="path-icon" width="74" height="82" viewBox="0 0 74 82" role="img" aria-label="Trading cards icon">
        <rect x="2" y="2" width="44" height="62" rx="4" fill="none" stroke="#17a9c4" stroke-width="3"/>
        <rect x="28" y="16" width="44" height="64" rx="4" fill="#fff" stroke="#17a9c4" stroke-width="3"/>
      </svg>
      <h2 class="path-title serif">Trading Cards</h2>
      <p class="path-desc">sports memorabilia - Handling cards for athletes from Junior Circuit to high school, college and beyond.</p>
    </a>
  </section>

  <section class="features">
    <div class="abs proof-panel"></div>
    <div class="abs proof-photo" role="img" aria-label="Photo of an open printed proposal brochure with city and resort images"></div>
    <p class="abs proof-name serif">ClearProof</p>
    <p class="abs proof-desc">See the actual product, with all your optional finishes and details, before your project goes to press.</p>

    <div class="abs tint-panel"></div>
    <div class="abs tint-photo" role="img" aria-label="Photo of a fanned colour swatch guide beside its box"></div>
    <p class="abs tint-name">TrueTint</p>
    <p class="abs tint-desc">95% of the Chromaref library without the hassle, cost or delay of special mixes.</p>
  </section>

  <section class="abs proto-band"></section>
  <div class="abs proto-photo" role="img" aria-label="Photo of business cards, pencils, eraser and glasses on a desk"></div>
  <h2 class="abs proto-title serif">Pre-Test Your Latest Concepts with Prototyping</h2>
  <p class="abs proto-sub">Prototyping allows you to review multiple versions of your design before you order.</p>

  <footer>
    <div class="abs foot-brand"><span class="brand-square"></span>vellamark</div>
    <div class="abs foot-col expect">
      <h3>Expect More</h3>
      <ul><li>All Products</li><li>TrueTint™</li><li>ClearProof™</li><li>Turnaround</li><li>Business Printing</li></ul>
    </div>
    <div class="abs foot-col about">
      <h3>About Us</h3>
      <ul><li>Creatives Only</li><li>Terms of Service</li><li>Privacy Policy</li><li>FAQ</li></ul>
    </div>
    <div class="abs foot-col contact">
      <h3>Contact Us</h3>
      <ul>
        <li><svg width="12" height="12" viewBox="0 0 24 24" aria-hidden="true"><path fill="#17a9c4" d="M6.6 10.8a15.1 15.1 0 0 0 6.6 6.6l2.2-2.2c.3-.3.7-.4 1-.2 1.1.4 2.3.6 3.6.6.6 0 1 .4 1 1V20c0 .6-.4 1-1 1A17 17 0 0 1 3 4c0-.6.4-1 1-1h3.5c.6 0 1 .4 1 1 0 1.3.2 2.5.6 3.6.1.3 0 .7-.2 1z"/></svg>855.GoVellamark (855.555.0148)</li>
        <li><svg width="12" height="12" viewBox="0 0 24 24" aria-hidden="true"><path fill="#17a9c4" d="M12 2a7 7 0 0 0-7 7c0 5 7 13 7 13s7-8 7-13a7 7 0 0 0-7-7zm0 9.5a2.5 2.5 0 1 1 0-5 2.5 2.5 0 0 1 0 5z"/></svg>Vellamark</li>
        <li class="indent">418 Harlow Lane</li>
        <li class="indent">Ridgefield (Dallas), TX 75410</li>
        <li><svg width="12" height="12" viewBox="0 0 24 24" aria-hidden="true"><path fill="#17a9c4" d="M2 5h20v14H2zm2 2v.5l8 5 8-5V7l-8 5z"/></svg>support@vellamark.com</li>
      </ul>
    </div>
    <div class="abs foot-rule"></div>
    <p class="abs copyright serif">Copyright ©2022 Vellamark.com. All Rights Reserved.</p>
    <div class="abs chat" aria-label="Chat">
      <svg width="26" height="24" viewBox="0 0 26 24" aria-hidden="true"><path fill="#fff" d="M13 2C6.9 2 2 6 2 11c0 2.6 1.3 4.9 3.5 6.5L4.5 22l4.8-2.5c1.2.3 2.4.5 3.7.5 6.1 0 11-4 11-9S19.1 2 13 2z"/><circle cx="8.5" cy="11" r="1.6" fill="#17a9c4"/><circle cx="13" cy="11" r="1.6" fill="#17a9c4"/><circle cx="17.5" cy="11" r="1.6" fill="#17a9c4"/></svg>
    </div>
  </footer>

</div>
</body>
</html>
```